Outdoor Street Sign in front of Commercial Building

I need a street sign roughly 4 feet tall and 6 feet wide. The sign will say “ PAINTLESS DENT REPAIR “. I need this sign to stand out and look Professional. I will provide photos of my shop and the location of this future sign. Color Scheme is very important to me.

Target Market(s)

People who own vehicles with Door Dings

Industry/Entity Type

Cosmetic Automobile Restoration

Font styles to use
Sans Serif
Other font styles liked:
• Gravity Normal, Kairos display solid, LTC square face small,

Colors

Designer to choose colors to be used in the design.

Requirements
Must have
• This street sign is simple in that it just needs to say “ PAINTLESS DENT REPAIR “. It is the creativity of the sign that is important to me. My commercial shop is on a busy street with a lot of traffic. My building really stands out and everyone can see my Company Name, which is Larkmoor Dent Repair. I need this sign to distinguish me from conventional body shops with the phrase “ PAINTLESS DENT REPAIR “. The whole point of this sign is for people driving by to do their own research on what Paintless Dent Repair is ?? If you can incorporate the same honeycomb pattern / design that is used as the background of my building sign, that would be great !!
Nice to have
• I’d like to see my company colors, which are red, black, and silver. Please be creative to somehow make this stand out. It would be nice to have the same honeycomb pattern / design that’s used as the background on the building sign to be used as the background of this sign !
Should not have
• This sign does not need any other information on it. Only the phrase “ PAINTLESS DENT REPAIR “

```html
<!DOCTYPE html>
<html lang="en">
<head>
<meta charset="utf-8">
<title>Paintless Dent Repair Street Sign</title>
<link rel="stylesheet" href="https://fonts.googleapis.com/css2?family=Orbitron:wght@900&family=Montserrat:wght@400&display=swap">
<style>
  :root {
    --board: #dedcdd;
    --honey-dark: #050505;
    --honey-mid: #1a1a1b;
    --band-left: #07080a;
    --band-right: #242424;
    --silver: #a7a9ac;
    --silver-light: #c9cacc;
    --silver-dark: #4a4b4d;
    --red: #c81e24;
    --caption: #1e1e1e;
  }
  html, body {
    margin: 0;
    padding: 0;
    width: 1200px;
    height: 861px;
    overflow: hidden;
    background: var(--board);
  }
  .canvas {
    position: relative;
    width: 1200px;
    height: 861px;
  }
  .street-sign {
    position: absolute;
    left: 97px;
    top: 85px;
    width: 1007px;
    height: 671px;
    display: block;
  }
  .sign-caption {
    position: absolute;
    left: 0;
    width: 1200px;
    top: 784px;
    margin: 0;
    text-align: center;
    font-family: "Montserrat", sans-serif;
    font-weight: 400;
    font-size: 24px;
    letter-spacing: 0.5px;
    color: var(--caption);
  }
  .headline {
    font-family: "Orbitron", sans-serif;
    font-weight: 900;
  }
  .headline-main { fill: var(--red); }
  .headline-sub { fill: var(--silver); }
</style>
</head>
<body>
<main class="canvas">
  <svg class="street-sign" viewBox="0 0 1007 671" xmlns="http://www.w3.org/2000/svg" aria-label="Paintless Dent Repair street sign">
    <defs>
      <radialGradient id="honeycombTone" cx="50%" cy="50%" r="75%">
        <stop offset="0%" stop-color="var(--honey-mid)"/>
        <stop offset="100%" stop-color="var(--honey-dark)"/>
      </radialGradient>
      <linearGradient id="bandTone" x1="0" y1="0" x2="1" y2="0">
        <stop offset="0%" stop-color="var(--band-left)"/>
        <stop offset="50%" stop-color="var(--band-left)"/>
        <stop offset="100%" stop-color="var(--band-right)"/>
      </linearGradient>
      <linearGradient id="silverTrim" x1="0" y1="0" x2="1" y2="0">
        <stop offset="0%" stop-color="var(--silver)"/>
        <stop offset="7%" stop-color="var(--silver-light)"/>
        <stop offset="28%" stop-color="var(--silver-dark)"/>
        <stop offset="40%" stop-color="var(--silver-light)"/>
        <stop offset="62%" stop-color="var(--silver-dark)"/>
        <stop offset="75%" stop-color="var(--silver)"/>
        <stop offset="88%" stop-color="var(--silver-dark)"/>
        <stop offset="100%" stop-color="var(--silver-light)"/>
      </linearGradient>
      <filter id="liftShadow" x="-5%" y="-20%" width="110%" height="150%">
        <feDropShadow dx="3" dy="4" stdDeviation="4" flood-color="#000" flood-opacity="0.8"/>
      </filter>
    </defs>

    <rect class="honeycomb-panel" x="0" y="0" width="1007" height="159" fill="url(#honeycombTone)" role="img" aria-label="Dark hexagonal honeycomb pattern"/>
    <rect class="honeycomb-panel" x="0" y="514" width="1007" height="157" fill="url(#honeycombTone)" role="img" aria-label="Dark hexagonal honeycomb pattern"/>

    <rect class="center-band" x="0" y="170" width="1007" height="333" fill="url(#bandTone)"/>
    <rect class="silver-trim" x="0" y="159" width="1007" height="11" fill="url(#silverTrim)"/>
    <rect class="silver-trim" x="0" y="503" width="1007" height="11" fill="url(#silverTrim)"/>

    <g filter="url(#liftShadow)">
      <text class="headline headline-main" x="55" y="336" font-size="118" textLength="896" lengthAdjust="spacingAndGlyphs">PAINTLESS</text>
      <text class="headline headline-sub" x="169" y="424" font-size="64" textLength="670" lengthAdjust="spacingAndGlyphs">DENT REPAIR</text>
    </g>
  </svg>
  <p class="sign-caption">Paintless Dent Repair Sign 03</p>
</main>
</body>
</html>
```